Recruiting agency needs corporate presentation

We are a recruiting agency specialized in life sciences. We need a corporate presentation that will be sent to our clients and prospects in a PDF format.

Details of the presentation:
- a "brochure" type of presentation, VERTICAL, with 5 pages (please see "content" file attached) The presentation will be sent in a PDF format to our prospect clients by e-mail, so the choice of images and organization need to take that into account.
- In the attachment, you will find our logo "Harlow & Associates".
- the presentation needs to convey our industry (life sciences, healthcare) and a high level of professionalism/leadership We want a sophisticated and elegant brochure.
- page 2 of the brochure needs to contain all the logos attached, in a very elegant, clear and organized way.
- page 3 shows a map with cursors (please see content file). The following countries/continents on the map need to be highlighted: USA, Brazil, Europe, North Africa, South Africa, China. We need "cursors" like pins to show where on the map our offices are: Miami, Boston, Lausanne, Denmark, Paris, Copenhaguen.
- page 4 includes pie charts (please see "Statistics 2020" Excel file): please improve the pie charts aesthetics, it needs to look very modern.

Target Market(s)

Healthcare / Life Sciences.

Requirements
Must have
• Very modern and aesthetics. I included a presentation of companies that we like to give you an indication of the overall style we're looking for.

```html
<!DOCTYPE html>
<html lang="en">
<head>
<meta charset="utf-8">
<title>Harlow &amp; Associates — Front cover options</title>
<link rel="stylesheet" href="https://fonts.googleapis.com/css2?family=Jost:wght@300;400;500;600&display=swap">
<style>
  :root {
    --page-bg: #dfe3ea;
    --navy: #1e3f60;
    --teal: #5bc3c9;
    --white: #ffffff;
    --ink: #1a1a1a;
    --caption: #2c4660;
    --photo-light: #c9d3e2;
    --photo-mid: #8e9fbe;
    --photo-dark: #4d5f83;
  }
  * { box-sizing: border-box; margin: 0; padding: 0; }
  html, body { width: 1200px; height: 2690px; overflow: hidden; }
  body {
    background: var(--page-bg);
    font-family: "Jost", "Futura", sans-serif;
    position: relative;
  }
  .options-title {
    position: absolute; top: 44px; left: 0; width: 1200px;
    text-align: center; font-weight: 300; font-size: 38px;
    color: var(--caption); letter-spacing: 0.01em;
  }
  .cover {
    position: absolute; left: 192px; width: 815px; height: 1153px;
    background: var(--navy);
    box-shadow: 0 10px 24px rgba(30, 50, 80, 0.18);
    overflow: hidden;
  }
  .cover--single { top: 144px; }
  .cover--columns { top: 1359px; }
  .cover__header {
    position: absolute; top: 0; left: 0; width: 100%; height: 178px;
    background: var(--white);
  }
  .brand { position: absolute; left: 77px; top: 100px; }
  .brand__name {
    display: flex; align-items: center; gap: 8px;
    font-weight: 600; font-size: 15px; letter-spacing: 0.12em;
    color: var(--ink); white-space: nowrap;
  }
  .brand__dot { width: 10px; height: 10px; border-radius: 50%; background: var(--ink); }
  .brand__tag {
    margin-top: 3px; font-weight: 500; font-size: 6.5px;
    letter-spacing: 0.16em; color: var(--ink); white-space: nowrap;
  }
  .cover__photo {
    position: absolute; top: 178px; left: 0; width: 100%; height: 555px;
    background:
      radial-gradient(ellipse at 40% 45%, rgba(230,236,245,0.75), transparent 55%),
      radial-gradient(ellipse at 78% 55%, rgba(215,224,238,0.6), transparent 45%),
      linear-gradient(180deg, var(--photo-light) 0%, var(--photo-mid) 55%, var(--photo-dark) 100%);
  }
  .headline {
    position: absolute; left: 77px; top: 612px;
    font-weight: 600; font-size: 57px; line-height: 60px;
    letter-spacing: 0.075em; text-transform: uppercase; white-space: nowrap;
  }
  .headline__line { display: block; }
  .headline__line--light { color: var(--white); }
  .headline__line--accent { color: var(--teal); }
  .intro {
    position: absolute; left: 77px; top: 870px; width: 670px;
    color: var(--white); font-size: 17.5px; line-height: 30.5px; font-weight: 400;
  }
  .intro p + p { margin-top: 11px; }
  .intro strong { font-weight: 600; }
  .intro--columns {
    top: 884px; width: 662px;
    display: grid; grid-template-columns: 1fr 1fr; column-gap: 31px;
  }
  .intro--columns p { text-align: justify; margin: 0 !important; }
  .site {
    position: absolute; top: 1073px;
    color: var(--teal); font-weight: 600; font-size: 21px; letter-spacing: 0.06em;
  }
  .site--right { right: 76px; }
  .site--center { left: 0; width: 100%; text-align: center; }
</style>
</head>
<body>
  <h1 class="options-title">Front cover options:</h1>

  <section class="cover cover--single">
    <header class="cover__header">
      <div class="brand">
        <div class="brand__name"><span class="brand__dot"></span>HARLOW &amp; ASSOCIATES</div>
        <div class="brand__tag">GLOBAL LIFE SCIENCES RECRUITING</div>
      </div>
    </header>
    <div class="cover__photo" role="img" aria-label="Scientists in white protective suits working with a microscope in a laboratory"></div>
    <h2 class="headline">
      <span class="headline__line headline__line--light">Best recruiters</span>
      <span class="headline__line headline__line--light">in life science.</span>
      <span class="headline__line headline__line--accent">Finding the best</span>
      <span class="headline__line headline__line--accent">talents worldwide</span>
    </h2>
    <div class="intro">
      <p>We are an international recruiting boutique agency specialized in life sciences. In the last 3 decades, we have appointed thousands of professionals globally.</p>
      <p>Our firm is known for being highly committed and able to deliver great results within budget and timing constraints.</p>
      <p><strong>Equality and parity are at the core of our activity.</strong></p>
    </div>
    <div class="site site--right">www.harlowassociates.com</div>
  </section>

  <section class="cover cover--columns">
    <header class="cover__header">
      <div class="brand">
        <div class="brand__name"><span class="brand__dot"></span>HARLOW &amp; ASSOCIATES</div>
        <div class="brand__tag">GLOBAL LIFE SCIENCES RECRUITING</div>
      </div>
    </header>
    <div class="cover__photo" role="img" aria-label="Scientists in white protective suits working with a microscope in a laboratory"></div>
    <h2 class="headline">
      <span class="headline__line headline__line--light">Best recruiters</span>
      <span class="headline__line headline__line--accent">in life science.</span>
      <span class="headline__line headline__line--accent">Finding the best</span>
      <span class="headline__line headline__line--accent">talents worldwide</span>
    </h2>
    <div class="intro intro--columns">
      <p>We are an international recruiting boutique agency specialized in life sciences. In the last 3 decades, we have appointed thousands of professionals globally.</p>
      <p>Our firm is known for being highly committed and able to deliver great results within budget and timing constraints. <strong>Equality and parity are at the core of our activity.</strong></p>
    </div>
    <div class="site site--center">www.harlowassociates.com</div>
  </section>
</body>
</html>
```